Personal Motivational Quote Poster Design

I would like to create a poster with some of my favorite quotes to hang in my office. I did similar projects in 2012 and 2014. I've uploaded the winning designs so you can get a better idea of what I'm looking for. I will provide feedback on your design within 24 hours of receiving it.

The poster must contain the following quotes:

“What the pupil must learn, if he learns anything at all, is that the world will do most of the work for you, provided you cooperate with it by identifying how it really works and aligning with those realities. If we do not let the world teach us, it teaches us a lesson.” - Walter Brindley

“I tackle every big new problem by asking two questions: Who has dealt with this problem well? And what can we learn from them?” - Hal Porter

“If we can really understand the problem, the answer will come out of it, because the answer is not separate from the problem.” - Ravel Ondashanti

“Success is nothing more than a few simple disciplines, practiced every day; while failure is simply a few errors in judgment, repeated every day. It is the accumulative weight of our disciplines and our judgments that leads us to either fortune or failure.” - Ned Calve

“Inaction breeds doubt and fear. Action breeds confidence and courage.” - Rex Halloway

“What’s the one thing you can do, such that by doing it, everything else will be easier or unnecessary?” - Lyle Danvers

Requirements
Must have
• The poster will be 24" high x 36" long and printed on canvas, so the image you create needs to have a resolution of at least 2700 x 3900.
Nice to have
• I don't have an exact vision for how the poster should look, so I am totally open to you using your creativity to develop, arrange and present the content as you'd like.

That said, I would like an image (photo or posterized image) of the person being quoted along with each quote. I do not have specific images that I would like you to use, so you will need to find the images on your own.

The images don't need to be perfect... I am more interested in the poster relating the essence of the quotes and the people being quoted than I am in perfect photographic images of the people being quoted.

```html
<!DOCTYPE html>
<html lang="en">
<head>
<meta charset="utf-8">
<title>Favorite Quotes Poster</title>
<link rel="stylesheet" href="https://fonts.googleapis.com/css2?family=Tinos:ital,wght@0,400;0,700;1,400&display=swap">
<style>
  :root {
    --bg-core: #3fa3ac;
    --bg-mid: #1f7380;
    --bg-edge: #0d3a44;
    --paper: #fbfaf4;
    --lemon: #f3ef3c;
    --tangerine: #ff7b16;
    --royal: #1848df;
    --raspberry: #e8175a;
    --lime: #3ef23c;
    --sun: #f6c300;
    --ink-dark: #1b1b1b;
    --ink-light: #ffffff;
    --portrait-a: #cfcfcf;
    --portrait-b: #6c6c6c;
  }
  * { box-sizing: border-box; margin: 0; padding: 0; }
  html, body { width: 800px; height: 1200px; overflow: hidden; }
  body { font-family: "Tinos", "Times New Roman", serif; }

  .poster {
    position: relative;
    width: 800px;
    height: 1200px;
    background:
      radial-gradient(ellipse at 45% 40%, var(--bg-core) 0%, var(--bg-mid) 55%, var(--bg-edge) 100%);
    overflow: hidden;
  }

  .strip {
    position: absolute;
    clip-path: polygon(0% 4%, 6% 0%, 14% 3%, 22% 0%, 31% 4%, 40% 1%, 49% 3%, 58% 0%, 67% 4%, 76% 1%, 85% 3%, 93% 0%, 100% 3%,
                       99% 50%, 100% 97%, 92% 100%, 84% 96%, 75% 100%, 66% 97%, 57% 100%, 48% 96%, 39% 100%, 30% 97%, 21% 100%, 12% 96%, 5% 100%, 0% 97%, 1% 50%);
    background: var(--paper);
    padding: 7px;
  }
  .strip-inner {
    width: 100%;
    height: 100%;
    clip-path: polygon(0% 3%, 8% 0%, 17% 4%, 26% 1%, 35% 3%, 44% 0%, 53% 4%, 62% 1%, 71% 3%, 80% 0%, 89% 4%, 100% 1%,
                       100% 98%, 91% 100%, 82% 96%, 73% 100%, 64% 97%, 55% 100%, 46% 96%, 37% 100%, 28% 97%, 19% 100%, 10% 96%, 0% 99%);
    display: flex;
    flex-direction: column;
    justify-content: center;
    padding: 14px 26px;
  }
  .quote { font-size: 16px; line-height: 1.28; }
  .author { font-size: 12px; margin-left: 4px; }
  .strip-right-text .strip-inner { padding-left: 30px; }
  .strip-under-portrait .strip-inner { padding: 10px 64px 10px 26px; }

  .tone-lemon .strip-inner { background: var(--lemon); color: var(--ink-dark); }
  .tone-tangerine .strip-inner { background: var(--tangerine); color: var(--ink-light); }
  .tone-royal .strip-inner { background: var(--royal); color: var(--ink-light); }
  .tone-raspberry .strip-inner { background: var(--raspberry); color: var(--ink-light); }
  .tone-lime .strip-inner { background: var(--lime); color: var(--ink-dark); }
  .tone-sun .strip-inner { background: var(--sun); color: var(--ink-dark); }

  .portrait {
    position: absolute;
    background: var(--paper);
    padding: 5px;
    box-shadow: 2px 3px 6px rgba(0,0,0,0.35);
  }
  .portrait-fill {
    width: 100%;
    height: 100%;
    background: linear-gradient(160deg, var(--portrait-a), var(--portrait-b));
  }
</style>
</head>
<body>
<main class="poster">

  <section class="strip tone-lemon strip-under-portrait" style="left:44px; top:22px; width:610px; height:168px;">
    <div class="strip-inner">
      <p class="quote">“What the pupil must learn, if he learns anything at all, is that the world will do most of the work for you, provided you cooperate with it by identifying how it really works and aligning with those realities. If we do not let the world teach us, it teaches us a lesson.” <span class="author">- Walter Brindley</span></p>
    </div>
  </section>
  <figure class="portrait" style="left:612px; top:32px; width:140px; height:136px;">
    <div class="portrait-fill" role="img" aria-label="Black and white portrait of Walter Brindley"></div>
  </figure>

  <section class="strip tone-tangerine strip-right-text" style="left:200px; top:198px; width:556px; height:144px;">
    <div class="strip-inner">
      <p class="quote">“I tackle every big new problem by asking two questions:<br>Who has dealt with this problem well?<br>And what can we learn from them?” <span class="author">- Hal Porter</span></p>
    </div>
  </section>
  <figure class="portrait" style="left:48px; top:204px; width:166px; height:124px;">
    <div class="portrait-fill" role="img" aria-label="Color portrait of Hal Porter"></div>
  </figure>

  <section class="strip tone-royal" style="left:44px; top:384px; width:574px; height:150px;">
    <div class="strip-inner">
      <p class="quote">“If we can really understand the problem, the answer will come out of it, because the answer is not separate from the problem.” <span class="author">- Ravel Ondashanti</span></p>
    </div>
  </section>
  <figure class="portrait" style="left:608px; top:354px; width:144px; height:174px;">
    <div class="portrait-fill" role="img" aria-label="Black and white portrait of Ravel Ondashanti"></div>
  </figure>

  <section class="strip tone-raspberry strip-right-text" style="left:206px; top:580px; width:550px; height:226px;">
    <div class="strip-inner">
      <p class="quote">“Success is nothing more than a few simple disciplines, practiced every day; while failure is simply a few errors in judgment, repeated every day. It is the accumulative weight of our disciplines and our judgments that leads us to either fortune or failure.” <span class="author">- Ned Calve</span></p>
    </div>
  </section>
  <figure class="portrait" style="left:48px; top:582px; width:170px; height:166px;">
    <div class="portrait-fill" role="img" aria-label="Black and white portrait of Ned Calve"></div>
  </figure>

  <section class="strip tone-lime" style="left:48px; top:852px; width:574px; height:142px;">
    <div class="strip-inner">
      <p class="quote">“Inaction breeds doubt and fear.<br>Action breeds confidence and courage.” <span class="author">- Rex Halloway</span></p>
    </div>
  </section>
  <figure class="portrait" style="left:608px; top:848px; width:144px; height:172px;">
    <div class="portrait-fill" role="img" aria-label="Black and white portrait of Rex Halloway"></div>
  </figure>

  <section class="strip tone-sun strip-right-text" style="left:206px; top:1040px; width:550px; height:136px;">
    <div class="strip-inner">
      <p class="quote">“What’s the one thing you can do, such that by doing it, everything else will be easier or unnecessary?” <span class="author">- Lyle Danvers</span></p>
    </div>
  </section>
  <figure class="portrait" style="left:48px; top:1040px; width:170px; height:134px;">
    <div class="portrait-fill" role="img" aria-label="Black and white portrait of Lyle Danvers"></div>
  </figure>

</main>
</body>
</html>
```